Vantor Holdings - Brochure - Industrial Construction Services

We need a brochure design based on the power point presentation attached. Our business is named Vantor Holdings and is an industrial project services business concentrating on Construction Project Management, Technical Services, and Consulting. We want to communicate that "We offer our clients a
unique systematic approach to solving technical challenges." As you can see from our logo designs we like the colors blue and grey. We are after clean, but innovative design overall. We also seem to like design that have darker style backgrounds. We would like this brochure to be a bi-fold 8.5"x 5.5" size when closed if possible. If any files or graphics are needed in original format please request them. Thanks!

Target Market(s)

Large Oil & Gas, Power Generation, and Engineering Companies.

Industry/Entity Type

Engineering

Font styles to use
Serif

Requirements
Must have
• A strong-lasting first impression.

```html
<!DOCTYPE html>
<html lang="en">
<head>
<meta charset="utf-8">
<title>Vantor Holdings Brochure</title>
<link href="https://fonts.googleapis.com/css2?family=Tinos:ital,wght@0,400;0,700;1,400&display=swap" rel="stylesheet">
<style>
:root{
  --navy:#1b1d5c;
  --navy-deep:#13154a;
  --red:#b42a30;
  --grey:#d4d6dc;
  --blue-mid:#3a55b0;
  --teal:#2a8fb0;
  --paper:#ffffff;
  --ink:#333;
  --bg:#eceef0;
}
*{margin:0;padding:0;box-sizing:border-box}
html,body{width:1200px;height:1200px;overflow:hidden;background:var(--bg);font-family:"Tinos",serif}
.canvas{position:relative;width:1200px;height:1200px}

.cover{position:absolute;left:165px;top:38px;width:840px;height:592px;
  background:linear-gradient(180deg,#1e2062 0%,var(--navy-deep) 100%);overflow:hidden;
  box-shadow:0 4px 14px rgba(0,0,0,.25)}
.values-band{position:absolute;left:157px;top:53px;width:525px;height:51px;background:var(--red);
  display:flex;justify-content:space-between;align-items:center;padding:0 14px 0 20px;
  color:#fff;font-weight:700;font-size:24px;letter-spacing:2px;font-variant:small-caps}
.brand-panel{position:absolute;left:64px;top:175px;width:731px;height:228px;border-radius:22px;
  background:rgba(70,80,160,.35)}
.brand-dot{position:absolute;left:136px;top:77px;width:70px;height:70px;border-radius:50%;background:var(--grey)}
.brand-name{position:absolute;left:278px;top:80px;color:var(--grey);font-size:46px;line-height:52px;
  font-variant:small-caps;letter-spacing:1px;white-space:nowrap}
.brand-rule{position:absolute;left:278px;top:137px;width:348px;height:2px;background:var(--grey)}
.brand-tagline{position:absolute;left:278px;top:146px;color:#fff;font-size:18px;letter-spacing:4.2px;
  text-transform:uppercase;white-space:nowrap}
.cover-waves{position:absolute;left:0;bottom:0;width:840px;height:115px;
  background:linear-gradient(180deg,rgba(31,58,138,0) 0%,rgba(35,106,160,.55) 45%,rgba(31,58,138,.8) 100%)}

.spread{position:absolute;left:42px;top:718px;width:1120px;height:420px;box-shadow:0 4px 14px rgba(0,0,0,.25)}
.page-left{position:absolute;left:0;top:0;width:545px;height:420px;background:var(--navy)}
.sidebar{position:absolute;left:0;top:0;width:163px;height:420px;background:var(--navy)}
.sidebar-name{position:absolute;left:71px;top:142px;transform:translate(-50%,-50%) rotate(-90deg);
  white-space:nowrap;color:var(--grey);font-size:28px;font-variant:small-caps}
.sidebar-tagline{position:absolute;left:97px;top:142px;transform:translate(-50%,-50%) rotate(-90deg);
  white-space:nowrap;color:#fff;font-size:11px;letter-spacing:2.6px;text-transform:uppercase}
.sidebar-dot{position:absolute;left:40px;top:297px;width:70px;height:70px;border-radius:50%;background:var(--grey)}
.photo{position:absolute;left:163px;top:0;width:382px;height:420px;
  background:linear-gradient(160deg,#5a6270 0%,#3a404c 55%,#2a2e3a 100%)}

.page-right{position:absolute;left:545px;top:0;width:575px;height:420px;background:var(--paper)}
.intro-header{position:absolute;left:0;top:0;width:575px;height:75px}
.intro-title{position:absolute;left:16px;top:24px;color:#fff;font-weight:700;font-size:24px}
.header-dot{position:absolute;left:412px;top:24px;width:28px;height:28px;border-radius:50%;background:var(--grey)}
.header-brand{position:absolute;left:456px;top:30px;color:#fff;font-size:12px;font-variant:small-caps;white-space:nowrap}
.header-tagline{position:absolute;left:456px;top:46px;color:#fff;font-size:5px;letter-spacing:1.2px;
  text-transform:uppercase;white-space:nowrap}
.columns{position:absolute;left:15px;top:88px;width:526px;display:flex;gap:12px;
  font-size:10px;line-height:14px;color:var(--ink);text-align:justify}
.col{width:257px}
.col p{margin-bottom:12px}
.welcome{color:var(--red);font-weight:700;font-size:15px;margin:2px 0 12px;text-align:left}
.signoff{text-align:right;font-size:10px}
.signature{font-style:italic;font-size:12px}
.web{position:absolute;left:215px;top:395px;font-size:8px;letter-spacing:2px;color:#444}
.page-num{position:absolute;left:521px;top:388px;font-size:17px;font-weight:700;color:var(--navy);
  border-bottom:3px solid var(--teal);padding:0 3px}
</style>
</head>
<body>
<div class="canvas">
  <section class="cover">
    <div class="values-band"><span>Knowledge</span><span>Integrity</span><span>Quality</span></div>
    <div class="brand-panel">
      <div class="brand-dot"></div>
      <div class="brand-name">Vantor Holdings</div>
      <div class="brand-rule"></div>
      <div class="brand-tagline">Management &amp; Consulting</div>
    </div>
    <div class="cover-waves" role="img" aria-label="Decorative flowing blue and teal wave artwork along the bottom of the cover"></div>
  </section>

  <section class="spread">
    <div class="page-left">
      <div class="sidebar">
        <div class="sidebar-name">Vantor Holdings</div>
        <div class="sidebar-tagline">Management &amp; Consulting</div>
        <div class="sidebar-dot"></div>
      </div>
      <div class="photo" role="img" aria-label="Portrait photo of the two founders standing side by side"></div>
    </div>
    <div class="page-right">
      <svg class="intro-header" viewBox="0 0 575 75" aria-hidden="true">
        <rect width="575" height="75" fill="#1b1d5c"/>
        <polygon points="330,0 575,0 575,75 385,75" fill="#e8e8ee"/>
        <polygon points="338,0 575,0 575,75 393,75" fill="#3a55b0"/>
      </svg>
      <div class="intro-title">INTRODUCTION</div>
      <div class="header-dot"></div>
      <div class="header-brand">Vantor Holdings</div>
      <div class="header-tagline">Management &amp; Consulting</div>
      <div class="columns">
        <div class="col">
          <div class="welcome">Welcome,</div>
          <p>We appreciate your time and the opportunity to introduce ourselves to you.</p>
          <p>Vantor Holdings was founded in 2007 by my father and I. We genuinely share a lifelong friendship established on mutual respect, wholehearted trust, and a compelling desire to make progress that benefits our surroundings.</p>
          <p>With over 60 years of diversely combined experience, my father with +45yrs. and myself with +15yrs., we have been blessed with countless opportunities to build genuine relationships with extremely talented individuals who commonly share similar moral beliefs and characteristics. We are grateful for their mutual trust in us and our teams' keen interest in exceeding expectations of our clients. We have extreme confidence in our resources and we are proud for them to represent us.</p>
        </div>
        <div class="col">
          <p>Our diverse experience in various industries enables us to offer our clients a unique systematic approach to solving technical challenges. We urge clients to engage us in discussions as early as project conception to offer our knowledge and various potential solutions to explore best options to accomplish objectives as efficiently as possible. We offer insight to clients to express our mutual interest in favorable results.</p>
          <p>We have successfully contributed to managing and executing many industrial construction projects ranging from small to large magnitude (mega projects) from concept to completion. We are confident our services will positively impact your bottom-line and contribute to your success.</p>
          <p>We look forward to speaking with you soon!</p>
          <div class="signoff"><div class="signature">Elliot Marsh</div>Founder CEO</div>
        </div>
      </div>
      <div class="web">WWW.VANTORHOLDINGS.COM</div>
      <div class="page-num">3</div>
    </div>
  </section>
</div>
</body>
</html>
```